Supplement Company Needs a Protein Powder Pouch Design

We are looking for a modern and fresh design for our 500g pouches of protein powder as our current design is not eye catching or exciting enough.

This new design will be printed on both sides of a 178mm x 280mm x 101mm pouch.

We have 4 flavours. These are Banana Ice Cream, Chocolate Deluxe, Strawberries & Cream and Vanilla Ice Cream.

Industry/Entity Type

Supplement

Requirements
Must have
• Attractive and eye catching front and space for all the nutritional information and ingredients on the back.

Must clearly state 'food supplement' somewhere on the front of the pouch.
Nice to have
• Our logo is attached.
Should not have
• No health claims as these are not allowed in the UK

```html
<!DOCTYPE html>
<html lang="en">
<head>
<meta charset="utf-8">
<title>Verda Supplements – Protein Powder Pouch</title>
<link rel="stylesheet" href="https://fonts.googleapis.com/css2?family=Bebas+Neue&family=Alfa+Slab+One&family=Montserrat:wght@400;500;600;800&display=swap">
<style>
  :root {
    --bg: #eceee8;
    --pouch: #262727;
    --pouch-edge: #1c1d1d;
    --lime: #a6cd3b;
    --white: #f7f7f5;
    --ink: #151515;
    --cocoa: #b9693d;
    --powder-a: #d6d7bc;
    --powder-b: #b4b891;
    --choc-a: #6a3219;
    --choc-b: #3c1a0c;
  }
  * { margin: 0; padding: 0; box-sizing: border-box; }
  html, body { width: 1200px; height: 800px; overflow: hidden; }
  body { background: var(--bg); font-family: "Montserrat", sans-serif; position: relative; }

  .pouch {
    position: absolute; left: 365px; top: 20px;
    width: 470px; height: 760px;
    background: linear-gradient(180deg, #2d2e2e 0%, var(--pouch) 40%, var(--pouch-edge) 100%);
    border-radius: 4px;
    overflow: hidden;
    box-shadow: 0 18px 30px rgba(0,0,0,0.18);
  }

  .spec-tab {
    position: absolute; left: 40px; top: 0; width: 82px; height: 195px;
    background: var(--lime); color: var(--ink); text-align: center;
  }
  .spec-tab .label {
    position: absolute; left: 0; right: 0; top: 110px;
    font-family: "Bebas Neue", sans-serif; font-size: 17px; line-height: 16px;
    padding-bottom: 4px; margin: 0 4px; border-bottom: 1.5px solid var(--ink);
  }
  .spec-tab .weight {
    position: absolute; left: 0; right: 0; top: 151px;
    font-family: "Bebas Neue", sans-serif; font-size: 14px;
  }
  .seal {
    position: absolute; left: 42px; top: 176px; width: 80px; height: 80px;
    border-radius: 50%; background: var(--white); border: 5px solid var(--pouch);
    box-shadow: 0 0 0 2px var(--white);
  }

  .quality-tabs { position: absolute; top: 0; left: 351px; display: flex; gap: 6px; }
  .quality-tab {
    width: 31px; height: 152px; border-radius: 0 0 16px 16px;
    display: flex; align-items: flex-end; justify-content: center; padding-bottom: 8px;
  }
  .quality-tab.green { background: var(--lime); }
  .quality-tab.white { background: var(--white); width: 37px; }
  .quality-tab span { width: 12px; height: 12px; border-radius: 50%; background: var(--ink); }

  .brand { position: absolute; left: 137px; top: 170px; color: var(--white); font-weight: 800; }
  .brand .name { display: block; font-size: 64px; line-height: 70px; letter-spacing: -1px; }
  .brand .tagline { display: block; font-size: 11px; letter-spacing: 7.4px; margin-top: -2px; padding-left: 3px; }

  .product-title { position: absolute; left: 98px; top: 268px; font-family: "Bebas Neue", sans-serif; }
  .product-title span { display: block; font-size: 112px; line-height: 84px; letter-spacing: 2px; }
  .product-title .protein { color: var(--lime); }
  .product-title .powder { color: var(--white); }

  .category-banner {
    position: absolute; left: 100px; top: 445px; width: 266px; height: 26px;
    background: var(--lime);
    clip-path: polygon(0 0, 100% 0, 96% 50%, 100% 100%, 0 100%, 4% 50%);
    font-family: "Alfa Slab One", serif; font-size: 18px; color: var(--ink);
    text-align: center; line-height: 27px; letter-spacing: 0.3px;
  }

  .powder-visual {
    position: absolute; left: 284px; top: 486px; width: 160px; height: 190px;
    background: radial-gradient(ellipse at 40% 40%, var(--powder-a), var(--powder-b));
    border-radius: 6px;
  }
  .flavour-visual {
    position: absolute; left: 34px; top: 540px; width: 132px; height: 80px;
    background: radial-gradient(ellipse at 50% 45%, var(--choc-a), var(--choc-b));
    border-radius: 8px;
  }

  .flavour { position: absolute; left: 44px; top: 630px; font-weight: 600; font-size: 22px; line-height: 25px; }
  .flavour .base { color: var(--cocoa); display: block; letter-spacing: 0.5px; }
  .flavour .variant { color: var(--white); display: block; }

  .stats { position: absolute; left: 46px; top: 696px; display: flex; gap: 7px; }
  .stat {
    width: 62px; height: 38px; border: 1.5px solid var(--white); border-radius: 3px;
    color: var(--white); text-align: center; font-size: 10px; line-height: 11px; padding-top: 5px;
  }
  .stat strong { display: block; font-size: 14px; line-height: 15px; font-weight: 800; }
  .stat.highlight { background: var(--lime); border-color: var(--lime); color: var(--ink); }

  .benefits {
    position: absolute; left: 330px; top: 686px; list-style: none;
    color: var(--white); font-size: 8.5px; line-height: 12px; font-weight: 500;
  }

  .base-band { position: absolute; left: 0; right: 0; top: 746px; height: 9px; background: var(--lime); }
</style>
</head>
<body>
  <main class="pouch">
    <div class="spec-tab">
      <div class="label">Protein<br>Supplement</div>
      <div class="weight">Net Wt.907G</div>
    </div>
    <div class="seal"></div>

    <div class="quality-tabs">
      <div class="quality-tab green"><span></span></div>
      <div class="quality-tab white"><span></span></div>
    </div>

    <div class="brand">
      <span class="name">VERDA</span>
      <span class="tagline">SUPPLEMENTS</span>
    </div>

    <h1 class="product-title">
      <span class="protein">PROTEIN</span>
      <span class="powder">POWDER</span>
    </h1>

    <div class="category-banner">FOOD SUPPLEMENT</div>

    <div class="powder-visual" role="img" aria-label="Leaf shapes filled with protein powder texture"></div>
    <div class="flavour-visual" role="img" aria-label="Chocolate pieces with a chocolate splash"></div>

    <div class="flavour">
      <span class="base">CHOCOLATE</span>
      <span class="variant">DELUXE FLAVOUR</span>
    </div>

    <div class="stats">
      <div class="stat"><strong>35G</strong>protein</div>
      <div class="stat highlight"><strong>100G</strong>Calories</div>
      <div class="stat"><strong>3G</strong>net carbs</div>
    </div>

    <ul class="benefits">
      <li>+ Guilt-free indulgence</li>
      <li>+ Mixed Instantly</li>
      <li>+ Zero Aspartame</li>
      <li>+ Clinically formulated</li>
    </ul>

    <div class="base-band"></div>
  </main>
</body>
</html>
```